K7GOODS PlumeRider shopify finish

I need finish.... I need k7goods logo as a thick and bold header, with the Rosalind Kettering logo brand in the corner of k7goods logo. I need this text right under header.... Invest in your potential , your pride, your profits.... i want that slogan to pop, so designers choice. I want a mix of black and white pictures of black families together and groups of black people together as the background. Contact Us: phone 555210-4817.... Email.. Martytalbot@k7goods.net
218 E Larkspur st.
Orlando FL
32871

Original PlumeRider flag print $40.00
PlumeRider flag Drawing print $40.00
Non KLD PlumeRider flag drawing print $40.00
The Lanternfolk Drawing print $40.00

Long sleeve $47.00
Hoodies $56.00
Also link to stitchly to put the Rosalind Kettering brand on tags

```html
<!DOCTYPE html>
<html lang="en">
<head>
<meta charset="utf-8">
<title>K7 Goods — Media and Merchandise</title>
<link href="https://fonts.googleapis.com/css2?family=Montserrat:ital,wght@0,400;0,500;0,600;0,700;1,700;1,800&display=swap" rel="stylesheet">
<style>
:root{
  --ink:#0c0519;
  --navy:#140a3c;
  --wine:#56090f;
  --wine-deep:#3d0508;
  --brand-red:#e0241b;
  --hero-a:#4a4a4a;
  --hero-b:#262626;
  --card:#f5f5f5;
  --line:#e6e6e6;
  --text:#333;
  --muted:#555;
  --white:#fff;
  --footer-text:#c9c4d4;
}
*{margin:0;padding:0;box-sizing:border-box}
html,body{width:1200px;height:2870px;overflow:hidden}
body{position:relative;background:var(--white);font-family:Arial,Helvetica,sans-serif;color:var(--text)}

/* header */
.site-header{position:absolute;left:0;top:0;width:1200px;height:156px;background:var(--ink);border-top:6px solid #3a0006;border-bottom:2px solid #2a0008}
.menu-toggle{position:absolute;left:113px;top:66px;display:flex;align-items:center;gap:12px;color:var(--white);font:500 17px 'Montserrat',sans-serif;letter-spacing:.5px}
.brand-row{position:absolute;left:352px;top:40px;width:470px;height:80px;display:flex;align-items:center;justify-content:space-between}
.brand-personal{font:500 20px 'Montserrat',sans-serif;color:#7fb6d8;display:flex;align-items:center;gap:10px}
.brand-personal .dot{width:14px;height:14px;border-radius:50%;background:#2b6fb0}
.brand-main{font:800 36px 'Montserrat',sans-serif;color:var(--brand-red);letter-spacing:1px}
.header-tools{position:absolute;right:110px;top:74px;display:flex;gap:26px;align-items:center}
.social-dot{width:14px;height:14px;border-radius:50%;background:var(--white)}

/* hero */
.hero{position:absolute;left:0;top:156px;width:1200px;height:702px;background:linear-gradient(120deg,var(--hero-a),var(--hero-b) 60%,#5b5b5b)}
.hero-title{position:absolute;left:668px;top:290px;color:var(--white);font:italic 800 72px 'Montserrat',sans-serif;letter-spacing:3px;line-height:1}
.hero-sub{position:absolute;left:668px;top:382px;color:var(--white);font:italic 700 33px 'Montserrat',sans-serif;letter-spacing:1.5px}
.hero-slogan{position:absolute;left:668px;top:448px;width:470px;padding:14px 20px;background:var(--wine);border-left:6px solid var(--brand-red);color:var(--white);font:italic 700 21px/30px 'Montserrat',sans-serif}

/* section heads */
.section-title{position:absolute;left:0;width:1200px;text-align:center;font:700 30px 'Montserrat',sans-serif;letter-spacing:2px;color:var(--navy)}
.section-title em{font-style:normal;color:var(--wine)}
.rule{position:absolute;left:571px;width:58px;height:3px;background:var(--wine)}

.intro{position:absolute;left:240px;top:986px;width:720px;text-align:center;font-size:14.5px;line-height:26px;color:var(--text)}

/* promo cards */
.promo{position:absolute;top:1113px;width:476px;height:412px;background:var(--card)}
.promo .shirt{position:absolute;left:80px;top:40px;width:316px;height:300px;border-radius:6px}
.promo .shop-btn{position:absolute;left:178px;top:215px;width:120px;height:44px;background:var(--wine-deep);color:var(--white);font:600 13px 'Montserrat',sans-serif;letter-spacing:1px;display:flex;align-items:center;justify-content:center;border-radius:2px}
.promo .label{position:absolute;left:0;right:0;top:356px;text-align:center;font:600 16px 'Montserrat',sans-serif;color:#222;letter-spacing:.5px}
.promo .label b{color:var(--wine);font-weight:600;margin-left:8px}

/* products */
.product{position:absolute;top:1700px;width:236px;height:296px;border:1px solid var(--line);text-align:center}
.product .art{position:absolute;left:25px;top:18px;width:186px;height:172px}
.product .price{position:absolute;left:0;right:0;top:196px;font:600 18px 'Montserrat',sans-serif;color:var(--wine)}
.product .name{position:absolute;left:10px;right:10px;top:228px;font:500 15.5px/22px 'Montserrat',sans-serif;color:#222}

/* news */
.news{position:absolute;top:2149px;width:313px}
.news .photo{width:313px;height:233px}
.news .date{margin-top:20px;font:600 20px 'Montserrat',sans-serif;color:var(--wine)}
.news h3{margin-top:14px;font:600 18px 'Montserrat',sans-serif;color:#222}
.news p{margin-top:12px;font-size:14px;line-height:26px;color:var(--muted)}

/* footer */
.site-footer{position:absolute;left:0;top:2603px;width:1200px;height:267px;background:var(--ink);color:var(--white)}
.footer-brand{position:absolute;left:124px;top:62px;font:800 40px 'Montserrat',sans-serif;color:var(--brand-red);letter-spacing:1px}
.footer-head{position:absolute;font:600 18px 'Montserrat',sans-serif;letter-spacing:1.5px}
.newsletter{position:absolute;left:464px;top:80px;display:flex}
.newsletter .field{width:270px;height:40px;background:var(--white);color:#444;font-size:15px;padding:11px 15px}
.newsletter .submit{width:92px;height:40px;background:var(--wine-deep);font:600 13px 'Montserrat',sans-serif;letter-spacing:1px;display:flex;align-items:center;justify-content:center}
.contact{position:absolute;left:124px;top:132px;font-size:13px;line-height:20px;color:var(--footer-text)}
.contact strong{color:var(--white);font-family:'Montserrat',sans-serif;font-weight:600;margin-right:6px}
.footer-social{position:absolute;left:911px;top:88px;display:flex;gap:26px}
.tag-link{position:absolute;left:911px;top:124px;font-size:13px;line-height:20px;color:var(--footer-text)}
.tag-link a{color:var(--white);text-decoration:underline}
.footer-divider{position:absolute;left:107px;right:112px;top:186px;height:1px;background:#241a33}
.cards{position:absolute;left:107px;top:216px;display:flex;gap:4px}
.cards span{width:37px;height:25px;border-radius:3px;background:var(--white)}
.copyright{position:absolute;right:112px;top:220px;font-size:14px}
</style>
</head>
<body>

<header class="site-header">
  <div class="menu-toggle">
    <svg width="24" height="20" viewBox="0 0 24 20"><rect y="1" width="24" height="3" fill="#fff"/><rect y="8.5" width="24" height="3" fill="#fff"/><rect y="16" width="24" height="3" fill="#fff"/></svg>
    MENU
  </div>
  <div class="brand-row">
    <div class="brand-personal"><span class="dot"></span>Rosalind Kettering</div>
    <div class="brand-main">K7GOODS</div>
  </div>
  <div class="header-tools">
    <span class="social-dot" aria-label="Social link"></span>
    <span class="social-dot" aria-label="Social link"></span>
    <svg width="18" height="18" viewBox="0 0 18 18" aria-label="Search"><circle cx="7.5" cy="7.5" r="5.5" fill="none" stroke="#fff" stroke-width="2.4"/><line x1="11.5" y1="11.5" x2="16.5" y2="16.5" stroke="#fff" stroke-width="2.6" stroke-linecap="round"/></svg>
    <svg width="20" height="18" viewBox="0 0 20 18" aria-label="Cart"><path d="M1 2h3l2 9h10l2-7H5" fill="none" stroke="#fff" stroke-width="2.2" stroke-linejoin="round"/><path d="M6 5h11l-1.6 5H7z" fill="#fff"/><circle cx="8" cy="15" r="1.7" fill="#fff"/><circle cx="15" cy="15" r="1.7" fill="#fff"/></svg>
  </div>
</header>

<section class="hero" role="img" aria-label="Black and white photo of a joyful couple posing on a vintage car on a mountain road">
  <h1 class="hero-title">K7GOODS</h1>
  <p class="hero-sub">MEDIA AND MERCHANDISE</p>
  <p class="hero-slogan">Invest in your potential, your pride, your profits.</p>
</section>

<h2 class="section-title" style="top:912px">WELCOME TO <em>K7 GOODS</em></h2>
<div class="rule" style="top:962px"></div>
<p class="intro">Sed ut perspiciatis unde omnis iste natus error sit voluptatem accusantium doloremque laudantium totam rem aperiam, eaque ipsa quae ab illo inventore veritatis et quasi architecto beatae vitae dicta explicabo. Nemo enim ipsam voluptatem quia voluptas sit aspernatur</p>

<div class="promo" style="left:111px">
  <div class="shirt" role="img" aria-label="Black long sleeve shirt with brand print" style="background:linear-gradient(180deg,#1d1a26,#111018)"></div>
  <div class="shop-btn">SHOP NOW</div>
  <div class="label">LONG SLEEVE<b>$47.00</b></div>
</div>
<div class="promo" style="left:613px">
  <div class="shirt" role="img" aria-label="Dark olive hoodie with brand print" style="background:linear-gradient(180deg,#2e3129,#1f211c)"></div>
  <div class="shop-btn">SHOP NOW</div>
  <div class="label">HOODIES<b>$56.00</b></div>
</div>

<h2 class="section-title" style="top:1609px">FEATURED <em>PRODUCTS</em></h2>
<div class="rule" style="top:1659px"></div>

<div class="product" style="left:111px">
  <div class="art" role="img" aria-label="Purple and white waving flag artwork" style="background:linear-gradient(180deg,#f3e8ea,#5a3a8a 55%,#2b1d4d)"></div>
  <div class="price">$40.00</div>
  <div class="name">ORIGINAL PLUMERIDER FLAG PRINT</div>
</div>
<div class="product" style="left:358px">
  <div class="art" role="img" aria-label="Drawn purple and white flag artwork" style="background:linear-gradient(180deg,#f3e8ea,#5a3a8a 55%,#2b1d4d)"></div>
  <div class="price">$40.00</div>
  <div class="name">PLUMERIDER FLAG DRAWING PRINT</div>
</div>
<div class="product" style="left:606px">
  <div class="art" role="img" aria-label="Drawn flag artwork with slogan lettering" style="background:linear-gradient(180deg,#f6eef0,#4e3486 55%,#e9e6ef)"></div>
  <div class="price">$40.00</div>
  <div class="name">NON KLD PLUMERIDER FLAG DRAWING PRINT</div>
</div>
<div class="product" style="left:853px">
  <div class="art" role="img" aria-label="Illustrated poster of a group of heroes" style="left:56px;width:124px;background:linear-gradient(180deg,#2a3c7a,#6b4a3a 60%,#1f2033)"></div>
  <div class="price">$40.00</div>
  <div class="name">THE LANTERNFOLK DRAWING PRINT</div>
</div>

<h2 class="section-title" style="top:2064px">LATEST <em>NEWS</em></h2>
<div class="rule" style="top:2113px"></div>

<article class="news" style="left:112px">
  <div class="photo" role="img" aria-label="Large format printer producing a colourful print" style="background:linear-gradient(180deg,#6a6a6e,#2c2c30 55%,#b67a3a)"></div>
  <div class="date">24 MAR 2021</div>
  <h3>Nemo enim ipsam voluptatem</h3>
  <p>Sed ut perspiciatis unde omnis iste natus error sit voluptatem accusantium doloremque lauda ntium, totam rem aperiam</p>
</article>
<article class="news" style="left:445px">
  <div class="photo" role="img" aria-label="Navy background scattered with red and white stars" style="background:linear-gradient(135deg,#1a1a5a,#26206e 50%,#3a1d5c)"></div>
  <div class="date">24 MAR 2021</div>
  <h3>Nemo enim ipsam voluptatem</h3>
  <p>Sed ut perspiciatis unde omnis iste natus error sit voluptatem accusantium doloremque lauda ntium, totam rem aperiam</p>
</article>
<article class="news" style="left:776px">
  <div class="photo" role="img" aria-label="Print worker inspecting a colour proof in a workshop" style="background:linear-gradient(180deg,#3d4a66,#1f2a44 55%,#c9b9a8)"></div>
  <div class="date">24 MAR 2021</div>
  <h3>Nemo enim ipsam voluptatem</h3>
  <p>Sed ut perspiciatis unde omnis iste natus error sit voluptatem accusantium doloremque lauda ntium, totam rem aperiam</p>
</article>

<footer class="site-footer">
  <div class="footer-brand">K7GOODS</div>
  <div class="footer-head" style="left:464px;top:46px">NEWSLETTER</div>
  <div class="newsletter">
    <div class="field">Email :</div>
    <div class="submit">SUBMIT</div>
  </div>
  <div class="contact"><strong>Contact Us:</strong>555210-4817 &nbsp;·&nbsp; Martytalbot@k7goods.net &nbsp;·&nbsp; 218 E Larkspur st., Orlando FL 32871</div>
  <div class="footer-head" style="left:911px;top:43px">GET CONNECTED</div>
  <div class="footer-social">
    <span class="social-dot" aria-label="Social link"></span>
    <span class="social-dot" aria-label="Social link"></span>
  </div>
  <p class="tag-link">Brand tags by <a href="#stitchly">stitchly</a></p>
  <div class="footer-divider"></div>
  <div class="cards" aria-label="Accepted payment methods">
    <span></span><span></span><span></span><span></span><span></span>
  </div>
  <p class="copyright">© Copyright 2021 K7 Goods.All Rights Reserved</p>
</footer>

</body>
</html>
```